Tall Pines Restaurant & Cafe Marketing is a is a marketing company that specialises in Restaurant Marketing.
We show independent restaurant owners how to increase profits & beat their competition, we advise our customers on direct marketing methods that will help to make customers more loyal to their restaurant.
I have included some images of logos that I like the look off.
The final design should communicate that our business is professional and polished. I look forward to seeing your designs.
Restaurant

```html
<!DOCTYPE html>
<html lang="en">
<head>
<meta charset="utf-8">
<title>Tall Pines Restaurant &amp; Cafe Marketing – Business Cards</title>
<link rel="stylesheet" href="https://fonts.googleapis.com/css2?family=Source+Sans+3:wght@500&display=swap">
<style>
  :root {
    --ink: #231f20;
    --paper: #ffffff;
    --card-edge: #9a9a9a;
    --backdrop: #ffffff;
  }
  html, body {
    margin: 0;
    padding: 0;
    width: 1200px;
    height: 900px;
    overflow: hidden;
    background: var(--backdrop);
  }
  .sheet {
    display: block;
    width: 1200px;
    height: 900px;
  }
  .wordmark {
    font-family: "Source Sans 3", "Frutiger", "Helvetica Neue", Arial, sans-serif;
    font-weight: 500;
    text-anchor: middle;
  }
  .wordmark__name { font-size: 47px; letter-spacing: 0.2px; }
  .wordmark__tagline { font-size: 22px; letter-spacing: 0.6px; }

  .card--light .card__face { fill: var(--paper); stroke: var(--card-edge); stroke-width: 1; }
  .card--light .card__plate,
  .card--light .card__cutlery { fill: var(--ink); }
  .card--light .wordmark { fill: var(--paper); }

  .card--dark .card__face { fill: var(--ink); }
  .card--dark .card__plate,
  .card--dark .card__cutlery { fill: var(--paper); }
  .card--dark .wordmark { fill: var(--ink); }
</style>
</head>
<body>
<svg class="sheet" viewBox="0 0 1200 900" xmlns="http://www.w3.org/2000/svg">
  <defs>
    <clipPath id="front-bounds"><rect x="282" y="47" width="636" height="377"/></clipPath>
    <clipPath id="back-bounds"><rect x="282" y="476" width="636" height="376"/></clipPath>
  </defs>

  <!-- Front: white card, dark plate -->
  <g class="card card--light">
    <rect class="card__face" x="282.5" y="47.5" width="635" height="376"/>
    <g clip-path="url(#front-bounds)">
      <circle class="card__plate" cx="603" cy="235" r="205"/>
      <rect class="card__cutlery" x="318" y="118" width="50" height="320" rx="6"
            role="img" aria-label="Fork silhouette"/>
      <rect class="card__cutlery" x="842" y="118" width="40" height="320" rx="14"
            role="img" aria-label="Table knife silhouette"/>
    </g>
    <text class="wordmark wordmark__name" x="601" y="235">Tall Pines</text>
    <text class="wordmark wordmark__tagline" x="601" y="267">Restaurant &amp; Cafe Marketing</text>
  </g>

  <!-- Back: dark card, white plate -->
  <g class="card card--dark">
    <rect class="card__face" x="282" y="476" width="636" height="376"/>
    <g clip-path="url(#back-bounds)">
      <circle class="card__plate" cx="603" cy="664" r="205"/>
      <rect class="card__cutlery" x="318" y="545" width="50" height="320" rx="6"
            role="img" aria-label="Fork silhouette"/>
      <rect class="card__cutlery" x="842" y="545" width="40" height="320" rx="14"
            role="img" aria-label="Table knife silhouette"/>
    </g>
    <text class="wordmark wordmark__name" x="601" y="664">Tall Pines</text>
    <text class="wordmark wordmark__tagline" x="601" y="695">Restaurant &amp; Cafe Marketing</text>
  </g>
</svg>
</body>
</html>
```